Professional & Modern Technology Business Card

We need a business card for our software/technology firm. Our services include Program/Project Management, Project Controls and Enterprise Analytics. Our clients are usually in the Aviation, Public Works, Transportation and Electric & Water Utility industries. We serve both public and private clients. Would like a very professional, conservative but somewhat modern design. Design, Develop, Deploy is the corporate tagline. We have two offices. The headquarters is in Atlanta, GA and a satellite office In Savannah, GA. Corporate Logo Attached.
Looking to do website and corporate brochure after the successful completion of this project. Would like to begin a working relationship with best designers.
Tagline: Design, Develop, Deploy
Website: www.quelvanesystems.example
My Name: Marla Dunstead
My Title: CEO
Email: mdunstead@quelvanesystems.example
Atlanta Address:
87 Corliss Avenue, #2291
Atlanta, GA 30301
Office: 404.555.0182
Fax: 404.555.0147
Mobile: 404.555.0163
Savannah Address:
350 West Harrow Bend Road
Suite 720
Savannah, GA 31401
Office: 912.555.0139
Fax: 404.555.0147
Mobile: 404.555.0163
Updates
Please include the email address in your designs: mdunstead@quelvanesystems.example.
I appreciate everyone's design efforts. Just a few notes:
1. Please remove the mobile number from the cards
2. The backs of the cards can be utilized for writing notes. Make sure your design on the back of the card is conducive to clearly adding writing if needed.
3. No black backgrounds please
4. Only use the corporate logo on the front of the card. You can use portions of the logo design, but not the logo in totality.
Thank You
Industry/Entity Type
Conservative
Look and feel
Each slider illustrates characteristics of the customer's brand and the style your logo design should communicate.

```html
<!DOCTYPE html>
<html lang="en">
<head>
<meta charset="utf-8">
<title>Quelvane Systems — Business Card</title>
<link rel="stylesheet" href="https://fonts.googleapis.com/css2?family=Arimo&family=Crimson+Text:wght@400;600&display=swap">
<style>
  :root {
    --stage: #ecebe8;
    --green: #a6cf4a;
    --green-deep: #8dbb2f;
    --green-light: #eef7d6;
    --green-rule: #9ccc3c;
    --ink: #1c1c1c;
    --ink-soft: #333333;
    --paper: #ffffff;
    --paper-soft: #f6f8f6;
    --bubble-shadow: #5f7a26;
    --chevron: #1e1e1e;
  }
  * { box-sizing: border-box; margin: 0; padding: 0; }
  html, body { width: 1200px; height: 1000px; overflow: hidden; }
  body {
    background: var(--stage);
    position: relative;
    font-family: "Crimson Text", Georgia, serif;
    color: var(--ink);
  }

  .side-label {
    position: absolute;
    font-family: "Arimo", Arial, sans-serif;
    font-size: 92px;
    color: #000;
    letter-spacing: 1px;
  }
  .side-label--front { left: 780px; top: 205px; }
  .side-label--back  { left: 150px; top: 730px; }

  .card {
    position: absolute;
    width: 620px;
    height: 360px;
    overflow: hidden;
    box-shadow: 0 6px 16px rgba(0,0,0,.22);
  }

  /* ---------- Front ---------- */
  .card--front {
    left: 130px; top: 110px;
    background: radial-gradient(ellipse 60% 70% at 50% 30%, var(--green-light) 0%, #c4e27f 45%, var(--green) 100%);
  }
  .front-bubble {
    position: absolute;
    left: 150px; top: 70px;
    width: 300px; height: 165px;
    background: var(--paper);
    box-shadow: 5px 6px 0 var(--bubble-shadow);
  }
  .front-bubble-tail {
    position: absolute;
    left: 355px; top: 228px;
  }
  .brand {
    position: absolute;
    left: 34px; top: 32px;
    display: flex; align-items: center; gap: 10px;
    font-size: 31px;
    line-height: 1.05;
    font-weight: 600;
    color: var(--ink);
    white-space: nowrap;
  }
  .brand-dot {
    width: 26px; height: 26px;
    border-radius: 50%;
    background: var(--green-deep);
    flex: none;
  }
  .tagline {
    position: absolute;
    left: 0; right: 0; top: 126px;
    text-align: center;
    font-size: 17px;
    letter-spacing: 2.5px;
    color: var(--ink-soft);
  }
  .front-web-tab {
    position: absolute;
    left: 150px; bottom: 0;
    width: 330px; height: 48px;
    background: var(--paper-soft);
    border-radius: 8px 8px 0 0;
    text-align: center;
    padding-top: 12px;
    font-size: 19px;
    font-weight: 600;
  }
  .front-stripe {
    position: absolute;
    bottom: 30px;
    height: 6px;
    background: var(--paper);
  }
  .front-stripe--left  { left: 0; width: 140px; }
  .front-stripe--right { right: 0; width: 132px; }

  /* ---------- Back ---------- */
  .card--back {
    left: 440px; top: 520px;
    background: var(--paper-soft);
  }
  .holder-name {
    position: absolute;
    left: 34px; top: 44px;
    font-size: 30px;
    font-weight: 600;
    font-variant: small-caps;
    letter-spacing: 1px;
  }
  .holder-title {
    position: absolute;
    left: 222px; top: 82px;
    font-size: 19px;
    color: var(--ink-soft);
  }

  .office {
    position: absolute;
  }
  .office--hq { left: 48px; top: 166px; }
  .office--satellite { left: 360px; top: 140px; }
  .office-heading {
    display: flex; align-items: center; gap: 6px;
    font-size: 19px;
    font-weight: 600;
    margin-bottom: 12px;
    white-space: nowrap;
  }
  .office-heading::before,
  .office-heading::after {
    content: ""; width: 24px; height: 4px; background: var(--ink-soft);
  }
  .contact-row {
    display: flex; align-items: flex-start; gap: 14px;
    font-size: 12.5px;
    line-height: 1.35;
    margin-bottom: 7px;
    white-space: nowrap;
  }
  .contact-row--address { margin-bottom: 10px; }
  .contact-icon { flex: none; width: 13px; height: 13px; margin-top: 1px; }
  .column-rule {
    position: absolute;
    left: 318px; top: 160px;
    width: 1px; height: 135px;
    background: var(--green-rule);
  }
  .email-band {
    position: absolute;
    left: 0; right: 0; bottom: 0;
    height: 50px;
    background: var(--green);
    display: flex; align-items: center; justify-content: center; gap: 12px;
    padding-right: 60px;
    font-size: 17px;
  }
  .email-band-chevron {
    position: absolute;
    right: 0; bottom: 0;
  }
</style>
</head>
<body>

  <div class="side-label side-label--front">FRONT</div>
  <div class="side-label side-label--back">BACK</div>

  <!-- Front of card -->
  <section class="card card--front" aria-label="Business card front">
    <div class="front-bubble">
      <div class="brand"><span class="brand-dot"></span><span>Quelvane<br>Systems, Inc.</span></div>
      <p class="tagline">Design|Develop|Deploy</p>
    </div>
    <svg class="front-bubble-tail" width="50" height="44" viewBox="0 0 50 44" aria-hidden="true">
      <polygon points="0,12 48,2 6,42" fill="var(--bubble-shadow)"/>
      <polygon points="0,0 44,0 4,36" fill="var(--paper)"/>
    </svg>
    <div class="front-stripe front-stripe--left"></div>
    <div class="front-stripe front-stripe--right"></div>
    <div class="front-web-tab">www.quelvanesystems.example</div>
  </section>

  <!-- Back of card -->
  <section class="card card--back" aria-label="Business card back">
    <h1 class="holder-name">Marla Dunstead</h1>
    <p class="holder-title">CEO</p>

    <div class="office office--hq">
      <h2 class="office-heading">Headquarters</h2>
      <div class="contact-row contact-row--address">
        <svg class="contact-icon" viewBox="0 0 13 13" aria-hidden="true"><rect width="13" height="13" rx="2" fill="var(--green)"/><path d="M6.5 2.5a2.5 2.5 0 0 1 2.5 2.5c0 2-2.5 5-2.5 5S4 7 4 5a2.5 2.5 0 0 1 2.5-2.5z" fill="#fff"/></svg>
        <span>87 Corliss Avenue, #2291<br>Atlanta, GA 30301</span>
      </div>
      <div class="contact-row">
        <svg class="contact-icon" viewBox="0 0 13 13" aria-hidden="true"><rect width="13" height="13" rx="2" fill="var(--green)"/><path d="M4 3l1.5 0 .7 2-1 .8a5 5 0 0 0 2 2l.8-1 2 .7V9.5c0 .5-.5 1-1 1A6 6 0 0 1 3 4c0-.5.5-1 1-1z" fill="#fff"/></svg>
        <span>404.555.0182</span>
      </div>
      <div class="contact-row">
        <svg class="contact-icon" viewBox="0 0 13 13" aria-hidden="true"><rect width="13" height="13" rx="2" fill="var(--green)"/><rect x="3" y="5" width="7" height="4.5" fill="#fff"/><rect x="4.5" y="3" width="4" height="2" fill="#fff"/></svg>
        <span>404.555.0147</span>
      </div>
    </div>

    <div class="column-rule"></div>

    <div class="office office--satellite">
      <h2 class="office-heading">Satellite Office</h2>
      <div class="contact-row contact-row--address">
        <svg class="contact-icon" viewBox="0 0 13 13" aria-hidden="true"><rect width="13" height="13" rx="2" fill="var(--green)"/><path d="M6.5 2.5a2.5 2.5 0 0 1 2.5 2.5c0 2-2.5 5-2.5 5S4 7 4 5a2.5 2.5 0 0 1 2.5-2.5z" fill="#fff"/></svg>
        <span>350 West Harrow Bend Road<br>Suite 720 Savannah, GA 31401</span>
      </div>
      <div class="contact-row">
        <svg class="contact-icon" viewBox="0 0 13 13" aria-hidden="true"><rect width="13" height="13" rx="2" fill="var(--green)"/><path d="M4 3l1.5 0 .7 2-1 .8a5 5 0 0 0 2 2l.8-1 2 .7V9.5c0 .5-.5 1-1 1A6 6 0 0 1 3 4c0-.5.5-1 1-1z" fill="#fff"/></svg>
        <span>912.555.0139</span>
      </div>
      <div class="contact-row">
        <svg class="contact-icon" viewBox="0 0 13 13" aria-hidden="true"><rect width="13" height="13" rx="2" fill="var(--green)"/><rect x="3" y="5" width="7" height="4.5" fill="#fff"/><rect x="4.5" y="3" width="4" height="2" fill="#fff"/></svg>
        <span>404.555.0147</span>
      </div>
    </div>

    <div class="email-band">
      <svg width="18" height="13" viewBox="0 0 18 13" aria-hidden="true"><rect x=".75" y=".75" width="16.5" height="11.5" fill="none" stroke="var(--ink)" stroke-width="1.3"/><path d="M1 1l8 6 8-6" fill="none" stroke="var(--ink)" stroke-width="1.3"/></svg>
      <span>mdunstead@quelvanesystems.example</span>
    </div>
    <svg class="email-band-chevron" width="92" height="72" viewBox="0 0 92 72" aria-hidden="true">
      <polygon points="10,0 92,0 92,72 22,72 36,50 0,22" fill="var(--paper-soft)"/>
      <polygon points="22,22 92,22 92,72 30,72 46,47" fill="var(--chevron)"/>
      <polygon points="10,0 92,0 92,22 22,22" fill="var(--chevron)"/>
    </svg>
  </section>

</body>
</html>
```